English and Spanish Language School Needs a Business Card

Need a business card design a startup company called Corvelle Language School. The company will offer English and Spanish conversational level courses designed to make the learner feel comfortable with grammar and vocabulary. We would like to see a logo with some colour that should communicate learning, growth.

Target Market(s)

Consumers and businesses

Industry/Entity Type

Education

Contact Information for Business Card

TBD

Font styles to use
Serif

Requirements
Must have
• Include the following
• Logo
• Name
• Title
• Cellphone Number
• Office Phone number
• Email address
• Office Address

```html
<!DOCTYPE html>
<html lang="en">
<head>
<meta charset="utf-8">
<title>Corvelle Language School – Business Card</title>
<link rel="stylesheet" href="https://fonts.googleapis.com/css2?family=Questrial&display=swap">
<style>
  :root {
    --red: #c8202f;
    --teal: #0aa5ad;
    --card: #f7f7f7;
    --ink: #3a3a3a;
    --rule: #c9c9c9;
    --backdrop: #e6e3de;
  }
  * { margin: 0; padding: 0; box-sizing: border-box; }
  html, body {
    width: 1200px; height: 1023px; overflow: hidden;
    background: var(--backdrop);
    font-family: "Questrial", "Century Gothic", sans-serif;
  }
  .card {
    position: absolute;
    width: 760px; height: 434px;
    left: 220px;
    background: var(--card);
    border-radius: 18px;
    overflow: hidden;
    box-shadow: 0 4px 14px rgba(0,0,0,.15);
  }
  .card--front { top: 48px; }
  .card--back  { top: 541px; }

  .band { position: absolute; }
  .band--top-teal    { left: 0; top: 0; width: 342px; height: 40px; background: var(--teal); }
  .band--top-red     { left: 342px; top: 0; right: 0; height: 22px; background: var(--red); }
  .band--bottom-red  { left: 0; bottom: 0; width: 430px; height: 22px; background: var(--red); }
  .band--bottom-teal { left: 430px; bottom: 0; right: 0; height: 40px; background: var(--teal); }

  .divider {
    position: absolute; left: 342px; top: 22px; bottom: 40px;
    border-left: 1px solid var(--rule);
  }

  .brand {
    position: absolute;
    display: flex; align-items: center; gap: 12px;
    color: var(--red);
  }
  .brand__dot { width: 16px; height: 16px; border-radius: 50%; background: var(--teal); flex: none; }
  .brand__name { font-weight: 400; line-height: 1.05; letter-spacing: .5px; }
  .brand__name span { display: block; }

  .card--front .brand { left: 40px; top: 250px; width: 280px; }
  .card--front .brand__name { font-size: 40px; }
  .card--front .brand__name span { font-size: 22px; margin-top: 4px; }

  .card--back .brand { left: 0; right: 0; top: 0; bottom: 0; justify-content: center; }
  .card--back .brand__name { font-size: 72px; }
  .card--back .brand__name span { font-size: 34px; margin-top: 4px; }
  .card--back .brand__dot { width: 24px; height: 24px; }

  .person { position: absolute; left: 390px; top: 96px; }
  .person__name { color: var(--red); font-size: 34px; font-weight: 400; letter-spacing: .5px; }
  .person__title { color: var(--red); font-size: 17px; margin-top: 2px; }

  .contact { position: absolute; left: 410px; top: 210px; list-style: none; }
  .contact li {
    display: flex; align-items: center; gap: 12px;
    color: var(--ink); font-size: 17px; height: 30px;
  }
  .contact svg { width: 15px; height: 15px; flex: none; }
</style>
</head>
<body>

<section class="card card--front" aria-label="Business card front">
  <div class="band band--top-teal"></div>
  <div class="band band--top-red"></div>
  <div class="band band--bottom-red"></div>
  <div class="band band--bottom-teal"></div>
  <div class="divider"></div>

  <div class="brand">
    <span class="brand__dot"></span>
    <p class="brand__name">Corvelle<span>Language School</span></p>
  </div>

  <div class="person">
    <h1 class="person__name">Your Name</h1>
    <p class="person__title">Title</p>
  </div>

  <ul class="contact">
    <li>
      <svg viewBox="0 0 16 16" aria-hidden="true"><path fill="#c8202f" d="M4 1l3 3-1.6 1.8a9 9 0 0 0 4.8 4.8L12 9l3 3-2 2.5C7 14 2 9 1.5 3z"/></svg>
      88-123-54321
    </li>
    <li>
      <svg viewBox="0 0 16 16" aria-hidden="true"><rect x="4" y="1" width="8" height="14" rx="1.5" fill="none" stroke="#c8202f" stroke-width="1.4"/><circle cx="8" cy="12.5" r=".9" fill="#c8202f"/></svg>
      88-123-54320
    </li>
    <li>
      <svg viewBox="0 0 16 16" aria-hidden="true"><rect x="1" y="3" width="14" height="10" fill="none" stroke="#c8202f" stroke-width="1.4"/><path d="M1 3l7 6 7-6" fill="none" stroke="#c8202f" stroke-width="1.4"/></svg>
      www.your web.com
    </li>
    <li>
      <svg viewBox="0 0 16 16" aria-hidden="true"><path fill="#c8202f" d="M8 1a5 5 0 0 0-5 5c0 4 5 9 5 9s5-5 5-9a5 5 0 0 0-5-5zm0 7a2 2 0 1 1 0-4 2 2 0 0 1 0 4z"/></svg>
      Your address
    </li>
  </ul>
</section>

<section class="card card--back" aria-label="Business card back">
  <div class="brand">
    <span class="brand__dot"></span>
    <p class="brand__name">Corvelle<span>Language School</span></p>
  </div>
</section>

</body>
</html>
```